INCREASED BUDGET -- Cover Art Template Needed For Record Label

We are an electronic music record label that needs a cover art template for our 2017 releases. The design must be easy to update in Photoshop with different text, colors, or patterns.

The winner will also be asked to design our social media banners for Facebook, Twitter, and SoundCloud, so there's an opportunity to make more money.

Words to describe our sound: sophisticated, forward-thinking, futuristic, modern, emotional

Please make the HA logo the focal point of your design. Feel free to modify our logo as needed. Bonus points for anyone that can find a way to visually represent the word "Harborline". Examples of artwork that we found attractive are included to provide inspiration.

You can view our previous releases by clicking on any of the links: https://www.trackvendor-example.com/label/harborline-audio/52741/releases

Target Market(s)

Electronic music lovers

Industry/Entity Type

Music Download

Font styles to use
Serif
Decorative
Other font styles liked:
• Aller Display, Aller Light

Requirements
Must have
• Harborline Audio record logo
• Name of artist: Owen Tarsley
• Title: Daybreak / Stay Close (Remixes)
Nice to have
• Tracklist:
• Stay Close (Brannok Remix)
• Daybreak (Velktone Remix)
• Catalog number: 382

```html
<!DOCTYPE html>
<html lang="en">
<head>
<meta charset="utf-8">
<title>Owen Tarsley – Daybreak / Stay Close (Remixes)</title>
<link rel="stylesheet" href="https://fonts.googleapis.com/css2?family=Montserrat:wght@400;600&display=swap">
<style>
  :root {
    --stage: #2e2e30;
    --sleeve: #4a4a4c;
    --art-pale: #a6a6a8;
    --art-light: #8c8c8e;
    --art-mid: #69696b;
    --art-dark: #38383a;
    --art-deep: #2c2c2e;
    --type: #f4f4f4;
    --type-soft: #dcdcdc;
  }
  html, body {
    margin: 0;
    padding: 0;
    width: 1200px;
    height: 780px;
    overflow: hidden;
    background: var(--stage);
  }
  .release-cover {
    position: absolute;
    left: 240px;
    top: 30px;
    width: 720px;
    height: 720px;
    background: var(--sleeve);
    overflow: hidden;
    font-family: "Montserrat", sans-serif;
    color: var(--type);
  }
  .cover-art {
    position: absolute;
    left: 0;
    top: 112px;
    width: 720px;
    height: 608px;
    background:
      radial-gradient(ellipse 22% 18% at 62% 12%, var(--art-pale) 0%, transparent 80%),
      radial-gradient(ellipse 20% 22% at 92% 10%, var(--art-light) 0%, transparent 85%),
      radial-gradient(ellipse 30% 25% at 42% 52%, var(--art-pale) 0%, transparent 80%),
      radial-gradient(ellipse 25% 30% at 20% 38%, var(--art-dark) 0%, transparent 85%),
      radial-gradient(ellipse 22% 30% at 4% 70%, var(--art-deep) 0%, transparent 85%),
      radial-gradient(ellipse 28% 22% at 70% 45%, var(--art-mid) 0%, transparent 80%),
      radial-gradient(ellipse 30% 25% at 38% 82%, var(--art-light) 0%, transparent 80%),
      radial-gradient(ellipse 28% 25% at 80% 85%, var(--art-dark) 0%, transparent 85%),
      linear-gradient(165deg, var(--art-mid) 0%, var(--sleeve) 50%, var(--art-dark) 100%);
  }
  .artist-name {
    position: absolute;
    left: 56px;
    top: 40px;
    margin: 0;
    font-size: 40px;
    font-weight: 600;
    line-height: 1;
    letter-spacing: 0.12em;
    text-transform: uppercase;
  }
  .release-title {
    position: absolute;
    left: 56px;
    top: 96px;
    margin: 0;
    font-size: 19px;
    font-weight: 400;
    line-height: 1;
    letter-spacing: 0.1em;
    text-transform: uppercase;
    color: var(--type-soft);
  }
  .catalog-number {
    position: absolute;
    right: 46px;
    top: 46px;
    font-size: 16px;
    font-weight: 400;
    letter-spacing: 0.04em;
    color: var(--type-soft);
  }
  .label-mark {
    position: absolute;
    left: 560px;
    top: 566px;
    display: flex;
    align-items: center;
    gap: 12px;
    font-size: 76px;
    font-weight: 600;
    line-height: 1;
    letter-spacing: 0.02em;
    color: var(--type);
  }
  .label-mark-square {
    width: 18px;
    height: 18px;
    background: var(--type);
  }
</style>
</head>
<body>
  <main class="release-cover">
    <div class="cover-art" role="img" aria-label="Abstract low-poly artwork of light and dark grey facets crossed by thin pale lines"></div>
    <h1 class="artist-name">Owen Tarsley</h1>
    <p class="release-title">Daybreak / Stay Close - Remixes</p>
    <span class="catalog-number">HA382</span>
    <div class="label-mark" aria-label="Harborline Audio">
      <span class="label-mark-square"></span>
      <span>HA</span>
    </div>
  </main>
</body>
</html>
```